Brightwell Rx Pass reinvent our website.

Our Website is outdated and needs an overhaul, in every aspect. We assist individuals that have little or no prescription coverage and allow them to receive a discount ranging from 33% up to 78% for free. In the beginning we utilized pharmacies to spread the word, but times have a changed. We are looking for a modern and clean site. We are open to anything, image, logo etc.

Northmark Market(s)

Anyone regardless of residency, age or income. This program is designed to assist those that have NO prescription coverage or for those whose particular prescription may not be covered by insurance.

Industry/Entity Type

Pharmaceutical

Coding

Coded - Design and coding required

Number of Pages Required

4 page

Requirements
Must have
• -The two MUST haves are the pharmacy locators & drug pricing. If you can combine the 2, even better.
• -a ongoing counter/tally on the 1stpage reflecting the amount of money we are saving customers. http://plumtreemarket.example/item/animated-counters-v-20-edge-animate-collection/full_screen_preview/52970314
• -on a smart phone the ability to view the information that is needed to get the actual discount for the medication.
Nice to have
• animated tutorial showing how to use the card
• health blog

```html
<!DOCTYPE html>
<html lang="en">
<head>
<meta charset="utf-8">
<title>Brightwell Rx Pass</title>
<link href="https://fonts.googleapis.com/css2?family=Source+Sans+3:wght@300;400;600;700&display=swap" rel="stylesheet">
<style>
  :root {
    --brand-blue: #0b4a9c;
    --brand-red: #e3262c;
    --text-dark: #444;
    --text-muted: #777;
    --white: #fff;
  }
  * { box-sizing: border-box; margin: 0; padding: 0; }
  html, body { width: 903px; height: 1200px; overflow: hidden; background: var(--white); }
  body { position: relative; font-family: "Source Sans 3", "Source Sans Pro", sans-serif; color: var(--text-dark); }
  .abs { position: absolute; }

  /* Header */
  .top-rule { left: 0; top: 0; width: 903px; height: 3px; background: var(--brand-blue); }
  .site-header { left: 0; top: 3px; width: 903px; height: 64px; background: var(--white); }
  .brand { left: 107px; top: 22px; display: flex; align-items: center; gap: 7px; }
  .brand-dot { width: 14px; height: 14px; border-radius: 50%; background: var(--brand-red); }
  .brand-name { font-size: 17px; font-weight: 600; color: var(--brand-blue); letter-spacing: .2px; }
  .main-nav a { position: absolute; top: 27px; font-size: 10.5px; color: #555; text-decoration: none; letter-spacing: .2px; }
  .main-nav a.is-active::after { content: ""; position: absolute; left: -9px; right: -9px; top: 19px; height: 2px; background: var(--brand-red); }
  .search-icon { left: 784px; top: 27px; }

  /* Hero */
  .hero-photo { left: 0; top: 67px; width: 903px; height: 427px;
    background: radial-gradient(ellipse at 68% 45%, #e6e6e6 0%, #bdbdbd 45%, #8f8f8f 100%); }
  .hero-panel { left: 108px; top: 197px; width: 359px; height: 179px; background: rgba(8, 66, 150, .93); padding: 14px 14px 0 14px; color: var(--white); }
  .hero-title { font-size: 17px; font-weight: 400; letter-spacing: .2px; margin-bottom: 8px; }
  .hero-list { list-style: none; }
  .hero-list li { font-size: 8.7px; font-weight: 300; line-height: 16.8px; display: flex; align-items: center; gap: 6px; }
  .hero-list svg { flex: none; }
  .btn { display: inline-block; font-weight: 700; font-size: 9.5px; color: var(--white); text-decoration: none; text-align: center; }
  .btn-red { position: absolute; left: 13px; top: 135px; width: 111px; height: 28px; line-height: 28px; background: var(--brand-red); }
  .slider-dots { left: 425px; top: 464px; display: flex; gap: 8px; }
  .slider-dots span { width: 7px; height: 7px; border-radius: 50%; background: #9a9a9a; }
  .slider-dots span.on { background: var(--brand-blue); }

  /* How to */
  .section-title { left: 0; width: 903px; text-align: center; top: 535px; font-size: 20px; font-weight: 400; color: #555; letter-spacing: .3px; }
  .savings-counter { left: 0; width: 903px; top: 569px; text-align: center; font-size: 10px; font-weight: 400; color: var(--text-muted); letter-spacing: .4px; }
  .savings-counter strong { font-size: 13px; font-weight: 700; color: var(--brand-red); letter-spacing: .6px; margin-right: 5px; }
  .step { top: 615px; width: 220px; text-align: center; }
  .step svg { display: block; margin: 0 auto; }
  .step-shadow { width: 90px; height: 4px; margin: 6px auto 14px; border-radius: 50%; background: radial-gradient(ellipse, #ccc 0%, rgba(204,204,204,0) 70%); }
  .step p { font-size: 10px; font-weight: 300; color: var(--text-muted); line-height: 17px; }

  /* Mission */
  .mission-band { left: 0; top: 799px; width: 903px; height: 233px;
    background: linear-gradient(90deg, #e6393b 0%, #e0393c 50%, #d93437 100%); }
  .mission-title { left: 107px; top: 824px; font-size: 20px; font-weight: 400; color: var(--white); letter-spacing: .3px; }
  .mission-text { left: 106px; top: 868px; width: 478px; font-size: 9.9px; font-weight: 300; line-height: 16.8px; color: var(--white); }
  .btn-blue { left: 107px; top: 969px; width: 110px; height: 34px; line-height: 34px; background: var(--brand-blue); }
  .mission-photo { left: 600px; top: 760px; width: 154px; height: 275px; border-radius: 77px 77px 6px 6px;
    background: linear-gradient(180deg, #d9c2b0 0%, #efe9e4 35%, #f7f7f7 70%, #e9e9e9 100%); }

  /* Footer */
  .footer-col { top: 1064px; width: 142px; }
  .footer-col h4 { font-size: 8.8px; font-weight: 600; color: var(--brand-blue); padding-bottom: 8px; border-bottom: 1px dotted #bbb; margin-bottom: 11px; letter-spacing: .1px; }
  .footer-col ul { list-style: none; }
  .footer-col li { font-size: 9px; color: #555; line-height: 14.5px; padding-left: 18px; position: relative; }
  .footer-col li::before { content: ""; position: absolute; left: 1px; top: 4px; border-left: 4px solid var(--brand-red); border-top: 3.5px solid transparent; border-bottom: 3.5px solid transparent; }
  .social { display: flex; gap: 9px; }
  .social span { width: 9px; height: 9px; background: var(--brand-red); }
  .footer-rule { left: 0; top: 1159px; width: 903px; height: 1px; background: #e6e6e6; }
  .copyright { left: 0; top: 1174px; width: 903px; text-align: center; font-size: 8.5px; color: #555; }
</style>
</head>
<body>
  <div class="abs top-rule"></div>
  <header class="abs site-header">
    <div class="abs brand"><span class="brand-dot"></span><span class="brand-name">Brightwell Rx Pass</span></div>
    <nav class="main-nav">
      <a class="is-active" style="left:338px">HOME</a>
      <a style="left:392px">GET CARD</a>
      <a style="left:464px">FAQ</a>
      <a style="left:509px">PHARMACIES</a>
      <a style="left:595px">DRUG PRICING</a>
      <a style="left:688px">CONTACT</a>
    </nav>
    <svg class="abs search-icon" width="11" height="11" viewBox="0 0 11 11"><circle cx="4.5" cy="4.5" r="3.3" fill="none" stroke="#e3262c" stroke-width="1.8"/><line x1="7" y1="7" x2="10" y2="10" stroke="#e3262c" stroke-width="2"/></svg>
  </header>

  <div class="abs hero-photo" role="img" aria-label="Smiling pharmacist holding a blister pack of tablets in a pharmacy, black and white"></div>
  <section class="abs hero-panel">
    <h1 class="hero-title">FREE PRESCRIPTION ASSITANCE PROGRAM</h1>
    <ul class="hero-list">
      <li><svg width="9" height="9" viewBox="0 0 9 9"><rect x=".5" y=".5" width="8" height="8" fill="none" stroke="#fff"/><path d="M2 4.5l2 2 4-5" fill="none" stroke="#fff" stroke-width="1.4"/></svg>&nbsp;Completely Free Prescription Assitance Program</li>
      <li><svg width="9" height="9" viewBox="0 0 9 9"><rect x=".5" y=".5" width="8" height="8" fill="none" stroke="#fff"/><path d="M2 4.5l2 2 4-5" fill="none" stroke="#fff" stroke-width="1.4"/></svg>Lowest Price logic to guarantee that you get the best deal on your prescriptions</li>
      <li><svg width="9" height="9" viewBox="0 0 9 9"><rect x=".5" y=".5" width="8" height="8" fill="none" stroke="#fff"/><path d="M2 4.5l2 2 4-5" fill="none" stroke="#fff" stroke-width="1.4"/></svg>Instant printable&nbsp; Membership card ready to use</li>
      <li><svg width="9" height="9" viewBox="0 0 9 9"><rect x=".5" y=".5" width="8" height="8" fill="none" stroke="#fff"/><path d="M2 4.5l2 2 4-5" fill="none" stroke="#fff" stroke-width="1.4"/></svg>Savings of upto 75% at more than than 60,000 national and regional pharmacies</li>
      <li><svg width="9" height="9" viewBox="0 0 9 9"><rect x=".5" y=".5" width="8" height="8" fill="none" stroke="#fff"/><path d="M2 4.5l2 2 4-5" fill="none" stroke="#fff" stroke-width="1.4"/></svg>This card is pre-activated and can be used immediately</li>
    </ul>
    <a class="btn btn-red">GET FREE CARD</a>
  </section>
  <div class="abs slider-dots"><span class="on"></span><span></span><span></span><span></span></div>

  <h2 class="abs section-title">HOW TO USE YOUR CARD</h2>
  <p class="abs savings-counter"><strong>$12,480,950</strong>SAVED BY OUR MEMBERS SO FAR</p>
  <div class="abs step" style="left:106px">
    <svg width="80" height="62" viewBox="0 0 80 62"><rect x="5" y="10" width="70" height="48" rx="4" fill="none" stroke="#0b4a9c" stroke-width="5"/><rect x="32" y="3" width="16" height="10" rx="3" fill="#0b4a9c"/><circle cx="23" cy="28" r="6" fill="#0b4a9c"/><path d="M13 47c0-8 5-11 10-11s10 3 10 11z" fill="#0b4a9c"/><rect x="40" y="24" width="26" height="4" fill="#0b4a9c"/><rect x="40" y="33" width="26" height="4" fill="#0b4a9c"/><rect x="40" y="42" width="26" height="4" fill="#0b4a9c"/></svg>
    <div class="step-shadow"></div>
    <p>Click "Get Free Card" button to print a copy of<br>your Brightwell Rx Pass.</p>
  </div>
  <div class="abs step" style="left:339px">
    <svg width="80" height="62" viewBox="0 0 80 62"><rect x="6" y="20" width="20" height="40" fill="#0b4a9c"/><rect x="54" y="20" width="20" height="40" fill="#0b4a9c"/><rect x="26" y="2" width="28" height="58" fill="#0b4a9c"/><rect x="36" y="6" width="8" height="18" fill="#fff"/><rect x="31" y="11" width="18" height="8" fill="#fff"/><rect x="35" y="44" width="10" height="16" fill="#fff"/><g fill="#fff"><rect x="10" y="26" width="4" height="4"/><rect x="17" y="26" width="4" height="4"/><rect x="10" y="35" width="4" height="4"/><rect x="17" y="35" width="4" height="4"/><rect x="10" y="44" width="4" height="4"/><rect x="17" y="44" width="4" height="4"/><rect x="59" y="26" width="4" height="4"/><rect x="66" y="26" width="4" height="4"/><rect x="59" y="35" width="4" height="4"/><rect x="66" y="35" width="4" height="4"/><rect x="59" y="44" width="4" height="4"/><rect x="66" y="44" width="4" height="4"/><rect x="31" y="30" width="4" height="4"/><rect x="45" y="30" width="4" height="4"/></g><rect x="2" y="59" width="76" height="3" fill="#0b4a9c"/></svg>
    <div class="step-shadow"></div>
    <p>The Brightwell Rx Pass is<br>accepted at all major pharmacies.</p>
  </div>
  <div class="abs step" style="left:576px">
    <svg width="80" height="62" viewBox="0 0 80 62"><g transform="rotate(-18 40 34)"><rect x="8" y="18" width="64" height="32" fill="none" stroke="#0b4a9c" stroke-width="5"/><circle cx="40" cy="34" r="8" fill="#0b4a9c"/><text x="40" y="38.5" text-anchor="middle" font-size="12" font-weight="700" fill="#fff" font-family="sans-serif">$</text></g><rect x="28" y="48" width="38" height="4" fill="#0b4a9c"/><rect x="28" y="54" width="38" height="4" fill="#0b4a9c"/></svg>
    <div class="step-shadow"></div>
    <p>Savings from 20-75% off most medications with<br>an average savings of 40%.</p>
  </div>

  <div class="abs mission-band" role="img" aria-label="Blurred pharmacy shelves tinted red"></div>
  <h2 class="abs mission-title">OUR MISSION</h2>
  <p class="abs mission-text">The Brightwell Rx Pass is a FREE prescription assistance program that is available to everyone regardless of residency, age or income. This program is designed to assist those with no prescription coverage or for those whose prescription is not covered by insurance.This card will provide you with Rx medication savings of up to 75% at more than 60,000 pharmacies across the country including Crestway/pharmacy, Maplegate, Fairpoint, Northmark, Linden Mart, Harborway, Tallpine, Quickmart, Ellery's, Hollis Tate, Fresh Acre and many more.</p>
  <a class="abs btn btn-blue">CONTACT US</a>
  <div class="abs mission-photo" role="img" aria-label="Smiling doctor in a white coat with a stethoscope, arms crossed"></div>

  <footer>
    <div class="abs footer-col" style="left:108px"><h4>SERVICES</h4><ul><li>Get Card</li><li>Pharmacy Search</li><li>Drug Pricing</li></ul></div>
    <div class="abs footer-col" style="left:284px"><h4>QUICK NAVIGATION</h4><ul><li>Home</li><li>FAQ</li><li>Contact</li></ul></div>
    <div class="abs footer-col" style="left:460px;width:152px"><h4>OTHER LINKS</h4><ul><li>Terms &amp; Conditions</li><li>Dispute Resolution Procedure</li></ul></div>
    <div class="abs footer-col" style="left:637px;width:98px"><h4>CONNECT WITH US</h4><div class="social"><span></span><span></span></div></div>
    <div class="abs footer-rule"></div>
    <p class="abs copyright">© 2016 Brightwell Rx Pass | All right are reserved.</p>
  </footer>
</body>
</html>
```